Basic loan proposal for mortgage broker needs wow factor design in Word

I have a basic word template that is quite ugly. I would like a designer to make it wow!

There are merge fields all over it and they need to be in there

My website is www.tovrenlending.com.au for logo

Home Loans

Home Loans

```html
<!DOCTYPE html>
<html lang="en">
<head>
<meta charset="utf-8">
<title>Tovren Lending – Preliminary Assessment &amp; Credit Proposal</title>
<link rel="stylesheet" href="https://fonts.googleapis.com/css2?family=Montserrat:wght@400;500;600;700;800&display=swap">
<style>
  :root {
    --backdrop: #9b9b9b;
    --paper: #ffffff;
    --ink: #111111;
    --grey-deep: #5e5e5e;
    --grey-mid: #8a8a8a;
    --grey-soft: #c8c8c8;
    --grey-pale: #e4e4e4;
    --night: #1c1c1c;
  }
  html, body { margin: 0; padding: 0; width: 700px; height: 1200px; overflow: hidden; background: var(--backdrop); }
  .stage {
    position: relative; width: 1469px; height: 2520px;
    transform: scale(0.47619); transform-origin: 0 0;
    font-family: "Montserrat", sans-serif; color: var(--ink);
  }

  /* ---------- front cover ---------- */
  .cover {
    position: absolute; left: 489px; top: 94px; width: 491px; height: 694px; overflow: hidden;
    background: linear-gradient(90deg, #c9c9c9 0%, #e6e6e6 30%, #f7f7f7 55%, var(--paper) 75%);
  }
  .cover-spine { position: absolute; left: 0; top: 0; width: 18px; height: 100%; background: linear-gradient(90deg, #f4f4f4, #bdbdbd); }
  .tagline { position: absolute; left: 0; width: 100%; margin: 0; text-align: center; font-weight: 400; }
  .tagline strong { font-weight: 700; }
  .cover .tagline { top: 28px; font-size: 15.5px; line-height: 18px; }
  .brand-name { position: absolute; left: 0; width: 100%; text-align: center; font-weight: 500; letter-spacing: -2px; line-height: 1; }
  .cover .brand-name { top: 160px; font-size: 104px; }
  .art { position: absolute; left: 0; top: 0; }

  /* ---------- spreads ---------- */
  .spread { position: absolute; width: 604px; height: 427px; overflow: hidden; background: var(--paper); }
  .page { position: absolute; top: 0; width: 302px; height: 427px; overflow: hidden; }
  .page.left { left: 0; background: var(--paper); }
  .page.right { left: 302px; background: linear-gradient(90deg, #d2d2d2 0%, #f0f0f0 6%, var(--paper) 14%); }
  .page.plain-right { background: var(--paper); }

  .back-cover { background: linear-gradient(180deg, var(--night) 0%, #2e2e2e 50%, #232323 100%); }
  .back-photo { position: absolute; inset: 0; background: radial-gradient(ellipse at 45% 45%, #4a4540 0%, #2b2927 50%, #1e1e1e 90%); }
  .back-title { position: absolute; top: 157px; left: 0; width: 100%; text-align: center; font-size: 21px; line-height: 28.5px; color: #6a6a6a; letter-spacing: 0.5px; }
  .back-title b { font-weight: 700; color: #7a7a7a; }
  .back-name { position: absolute; top: 352px; left: 0; width: 100%; text-align: center; font-size: 38px; font-weight: 500; letter-spacing: -1px; color: var(--paper); line-height: 1; }
  .back-url { position: absolute; top: 401px; left: 0; width: 100%; text-align: center; font-size: 9.5px; color: var(--paper); }

  .front-mini .tagline { top: 18px; font-size: 9.5px; line-height: 11px; }
  .front-mini .brand-name { top: 92px; font-size: 64px; }

  .page-logo { position: absolute; top: 5px; font-size: 15px; font-weight: 500; letter-spacing: -0.5px; line-height: 1; }
  .left .page-logo { left: 9px; }
  .right .page-logo { right: 9px; }
  .band { position: absolute; left: 0; top: 27px; width: 604px; height: 21px; background: var(--ink); }
  .band-label { position: absolute; top: 34px; font-size: 5.6px; font-weight: 500; color: var(--paper); letter-spacing: 0.2px; }
  .band-label.l { left: 9px; }
  .band-label.r { right: 9px; }
  .gutter-mark { position: absolute; left: 252px; top: 0; }

  .footer-rule { position: absolute; left: 0; top: 410px; width: 604px; height: 1.5px; background: var(--ink); }
  .footer-text { position: absolute; top: 415px; font-size: 4.3px; font-weight: 600; }
  .ft-l1 { left: 12px; } .ft-r1 { left: 275px; }
  .ft-l2 { left: 314px; } .ft-r2 { right: 12px; }

  .body { position: absolute; top: 78px; left: 10px; width: 282px; font-size: 4.3px; line-height: 5.3px; }
  .right .body { left: 10px; }
  .body p { margin: 0 0 2.6px; }
  .h1 { font-size: 8.2px; line-height: 9.5px; font-weight: 700; margin: 0 0 5px; }
  .h2 { font-size: 6.4px; line-height: 7.5px; font-weight: 700; margin: 5px 0 2px; }
  .h3 { font-size: 4.6px; line-height: 5.6px; font-weight: 700; margin: 4px 0 1.5px; }
  .mf { margin: 0 0 2.6px; }
  .just { text-align: justify; }
  .details { display: grid; grid-template-columns: 146px 1fr; row-gap: 0.4px; margin-bottom: 8px; }
  .details b { font-weight: 700; }
  .bullets { margin: 0 0 3px; padding-left: 18px; }
  .bullets li { margin-bottom: 2.6px; }
  .list-mf p { margin-bottom: 4.1px; }
</style>
</head>
<body>
<div class="stage">

  <!-- Front cover -->
  <section class="cover">
    <div class="cover-spine"></div>
    <p class="tagline">Australia’s #1<br><strong>Home Loan</strong> Specialist<br>for Medical Professionals</p>
    <div class="brand-name">tovren</div>
    <svg class="art" width="491" height="694" viewBox="0 0 491 694">
      <defs>
        <linearGradient id="coverGrey" x1="0" y1="1" x2="1" y2="0">
          <stop offset="0" stop-color="#5a5a5a"/><stop offset="0.55" stop-color="#999"/><stop offset="1" stop-color="#c9c9c9"/>
        </linearGradient>
        <linearGradient id="photoTone" x1="0" y1="0" x2="1" y2="1">
          <stop offset="0" stop-color="#e2e4e6"/><stop offset="0.5" stop-color="#b8b1a6"/><stop offset="1" stop-color="#6c7a8c"/>
        </linearGradient>
        <filter id="lift" x="-20%" y="-20%" width="140%" height="140%">
          <feDropShadow dx="0" dy="5" stdDeviation="5" flood-color="#000" flood-opacity="0.45"/>
        </filter>
      </defs>
      <polygon points="245,341 491,587 491,611 408,694 83,694 0,611 0,587" fill="url(#coverGrey)"/>
      <polygon points="245,307 347,409 245,511 143,409" fill="var(--ink)"/>
      <g filter="url(#lift)">
        <polygon points="245,386 391,532 245,676 100,532" fill="url(#photoTone)" stroke="#fff" stroke-width="4"
                 role="img" aria-label="Photo of a couple embracing in front of a modern two-storey home"/>
      </g>
    </svg>
  </section>

  <!-- Spread: back & front covers -->
  <section class="spread" style="left:110px; top:911px;">
    <div class="page left back-cover">
      <div class="back-photo" role="img" aria-label="Dimmed photo of a smiling family at home"></div>
      <div class="back-title">INCOME<br><b>PROTECTION</b><br>AND<br><b>LIFE INSURANCE</b></div>
      <div class="back-name">tovren</div>
      <div class="back-url">www.tovrenlending.com.au</div>
    </div>
    <div class="page right front-mini" style="background:linear-gradient(90deg,#cfcfcf 0%,#ececec 35%,#fff 65%);">
      <p class="tagline">Australia’s #1<br><strong>Home Loan</strong> Specialist<br>for Medical Professionals</p>
      <div class="brand-name">tovren</div>
      <svg class="art" width="302" height="427" viewBox="0 0 302 427">
        <defs>
          <linearGradient id="miniGrey" x1="0" y1="1" x2="1" y2="0">
            <stop offset="0" stop-color="#5a5a5a"/><stop offset="1" stop-color="#b5b5b5"/>
          </linearGradient>
          <linearGradient id="miniPhoto" x1="0" y1="0" x2="1" y2="1">
            <stop offset="0" stop-color="#e2e4e6"/><stop offset="0.5" stop-color="#b8b1a6"/><stop offset="1" stop-color="#6c7a8c"/>
          </linearGradient>
          <filter id="miniLift" x="-20%" y="-20%" width="140%" height="140%">
            <feDropShadow dx="0" dy="3" stdDeviation="3" flood-color="#000" flood-opacity="0.45"/>
          </filter>
        </defs>
        <polygon points="151,220 302,371 302,427 0,427 0,371" fill="url(#miniGrey)"/>
        <polygon points="151,190 213,252 151,314 89,252" fill="var(--ink)"/>
        <g filter="url(#miniLift)">
          <polygon points="151,240 241,330 151,420 61,330" fill="url(#miniPhoto)" stroke="#fff" stroke-width="3"
                   role="img" aria-label="Photo of a couple embracing in front of a modern two-storey home"/>
        </g>
      </svg>
    </div>
  </section>

  <!-- Spread: pages 01–02 -->
  <section class="spread" style="left:769px; top:911px;">
    <div class="page left">
      <div class="page-logo">tovren</div>
      <div class="body">
        <div class="h1" style="margin-top:2px;">PRELIMINARY ASSESSMENT &amp; CREDIT PROPOSAL</div>
        <p style="margin-top:8px;">Issue date: {system.currentDate}</p>
        <div class="h3" style="margin-top:6px;">ABOUT YOU</div>
        <p class="mf">{{brokerToolsTablesBorrowers}}</p>
        <div class="h3" style="margin-top:8px;">ABOUT US</div>
        <div class="h3" style="margin-top:6px; font-size:4px;">BROKER DETAILS</div>
        <div class="details">
          <span>BROKER</span><b>{DEAL.OWNER.NAMEFULL}</b>
          <span>Credit Representative Name</span><span>{deal.owner.license.institution1}</span>
          <span>Credit Representative Number</span><span>{deal.owner.license.id1}</span>
          <span>{deal.owner.license.institution4} Member Number</span><span>{deal.owner.license.id4}</span>
          <span>Business Name</span><span>{deal.owner.license.institution5}</span>
          <span>Address</span><span>{deal.owner.address}</span>
          <span>Phone Number</span><span>{deal.owner.phone}</span>
          <span>Email</span><span>{deal.owner.email}</span>
        </div>
        <div class="h3" style="font-size:4px;">LICENSEE DETAILS</div>
        <div class="details">
          <span>AUSTRALIAN CREDIT LICENCE NAME</span><span>{ORGANIZATION.LICENSE.INSTITUTION1}</span>
          <span>Australian Credit Licence Number</span><span>{organization.license.id1}</span>
          <span>Business Name</span><span>{organization.license.institution4}</span>
          <span>Address</span><span>{organization.license.institution2}</span>
          <span>Phone Number</span><span>{organization.license.id3}</span>
          <span>Email</span><span>{organization.license.institution3}</span>
        </div>
        <p>If your Broker is a Credit Representative, this Preliminary Assessment &amp; Credit Proposal is being provided on behalf of the Licensee.</p>
        <div class="h3" style="font-size:5.2px; margin-top:8px;">ABOUT THIS PRELIMINARY ASSESSMENT &amp; CREDIT PROPOSAL</div>
        <p>This Preliminary Assessment &amp; Credit Proposal sets out important information that we must give you when we provide you with credit assistance.</p>
        <p style="margin-top:4px;">This document outlines:</p>
        <p>- the information provided by you in relation to your financial situation, requirements and objectives;</p>
      </div>
    </div>
    <div class="page right">
      <div class="page-logo">tovren</div>
      <div class="body" style="top:76px;">
        <ul class="bullets">
          <li>the preliminary assessment we completed to ensure we recommended a loan which is not unsuitable for you;</li>
          <li>our recommendation and why we believe this is in your best interests;</li>
          <li>fees and charges payable; and</li>
          <li>commissions that we or other parties may receive in relation to the proposed loan/s.</li>
        </ul>
        <p>Please read through and sign the Client Acknowledgement to indicate that the content is true and correct at the time of signing.</p>
        <div class="h2">PRELIMINARY ASSESSMENT &amp; CREDIT PROPOSAL</div>
        <div class="h3">ASSESSMENT DETAILS</div>
        <p>We have based this assessment on the information provided by you in the Client Needs Analysis. We have assessed that this particular credit application is NOT UNSUITABLE for you. This assessment is valid for 90 days from the date it has been issued.</p>
        <div class="h3" style="font-size:5.2px;">MONTHLY FINANCIAL POSITION</div>
        <p>A summary of your current versus proposed monthly financial position (including a buffer/floor rate) is set out below. The calculations are based on the information you provided and we verified.</p>
        <p class="mf">{{brokerToolsTablesMonthlyFinancialPositionBuffer}}</p>
        <p>* Buffer is calculated as: 80.00% of rental income added to gross income, 3.00% buffer on current mortgage rates, 5.25% as floor rate on proposed loan rates.</p>
        <div class="h3" style="font-size:5.2px; margin-top:6px;">NEEDS &amp; OBJECTIVES</div>
        <div class="h3" style="font-size:4px;">PRIMARY REASONS FOR SEEKING CREDIT/YOUR NEEDS &amp; OBJECTIVES</div>
        <p class="mf">{DEAL.OBJECTIVES.NEEDSANDOBJECTIVES.NOTES}</p>
        <div class="h3" style="font-size:4px;">IMMEDIATE NEEDS &amp; OBJECTIVES - WITHIN THE NEXT TWO YEARS (E.G. HOLIDAY, PURCHASES, RENOVATIONS, SAVINGS, PROTECT THE FAMILY, ETC.)</div>
        <p class="mf">{deal.objectives.needsAndObjectives.immediateNeedsAndObjectivesNotes}</p>
        <div class="h3" style="font-size:4px;">LONGER TERM - BETWEEN 2 TO 10 YEARS' TIME (E.G. REPAY MORTGAGE, BUY A NEW CAR, EDUCATION EXPENSES, PURCHASE INVESTMENT PROPERTY, RETIREMENT PLANNING, ETC)</div>
        <p class="mf">{deal.objectives.needsAndObjectives.longerTermNotes}</p>
        <div class="h3" style="font-size:5.2px;">REQUIREMENTS &amp; OBJECTIVES</div>
        <p class="mf" style="margin:0;">{{dealTablesLoanPurpose}}</p>
        <p class="mf">{{dealTablesRequirementsAndObjectives}}</p>
      </div>
    </div>
    <div class="band"></div>
    <span class="band-label l">INCOME PROTECTION &amp; LIFE INSURANCE</span>
    <span class="band-label r">INCOME PROTECTION &amp; LIFE INSURANCE</span>
    <svg class="gutter-mark" width="100" height="80" viewBox="0 0 100 80"><polygon points="20,19 38,37 20,55 2,37" fill="var(--grey-mid)"/><polygon points="80,19 98,37 80,55 62,37" fill="var(--grey-mid)"/><polygon points="50,0 87,37 50,74 13,37" fill="var(--ink)"/></svg>
    <div class="footer-rule"></div>
    <span class="footer-text ft-l1">PRELIMINARY ASSESSMENT &amp; CREDIT PROPOSAL 07/2021</span>
    <span class="footer-text ft-r1">01 OF 11</span>
    <span class="footer-text ft-l2">PRELIMINARY ASSESSMENT &amp; CREDIT PROPOSAL 07/2021</span>
    <span class="footer-text ft-r2">02 OF 11</span>
  </section>

  <!-- Spread: pages 03–04 -->
  <section class="spread" style="left:110px; top:1432px;">
    <div class="page left">
      <div class="page-logo">tovren</div>
      <div class="body" style="top:83px;">
        <div class="h3" style="font-size:5.4px; margin-top:0;">PRODUCT REQUIREMENTS</div>
        <p>This is a summary of the specific loan features you have requested. Please ensure you have read and understood the characteristics associated with each feature.</p>
        <p class="mf">{{dealTablesProductRequirementsSummary}}</p>
        <div class="h3" style="font-size:5.4px;">BROKER DISCLOSURE</div>
        <p class="mf">{{brokerToolsTablesBrokerDisclosure}}</p>
        <p style="margin-top:4px;">* Please refer to the Risks/Benefits Statements which covers the risks and benefits of your requested loan features.</p>
        <div class="h3" style="font-size:5.4px;">WHAT IS MOST IMPORTANT FOR YOU?</div>
        <p class="mf">{{dealTablesWhatIsMostImportantForYou}}</p>
        <div class="h3" style="font-size:5.4px;">TERM OF CREDIT SOUGHT</div>
        <p class="mf">{{dealTablesTermOfCreditSought}}</p>
        <div class="h3" style="font-size:5.4px;">BROKER ANALYSIS</div>
        <div class="h3" style="font-size:4px; margin-top:5px;">ANALYSIS, ASSESSMENT AND APPLICANT EDUCATION COMMENTS</div>
        <p class="mf">{BROKERTOOLS.ADVICECOMMENTS.ANALYSISCOMMENTS}</p>
        <div class="h3" style="font-size:5.4px;">LOAN PRODUCTS/FEATURES COMPARED</div>
        <p class="just">Based on the information provided by you, we compared the following lenders and products before making our recommendation:</p>
        <p class="mf">{{brokerToolsTablesCompareProductsComplex}}</p>
        <p>* Lenders Mortgage Insurance (LMI) is allocated to the primary split of the proposed loan product. This allocation may vary in accordance with your requirements and/or the lender's credit criteria.</p>
        <p class="mf" style="margin-top:4px; margin-bottom:0;">{%brokerToolsChartsCompareProducts}</p>
        <p>* The above chart shows the principal, interest and fees payable for the compared loan/s.</p>
      </div>
    </div>
    <div class="page right">
      <div class="page-logo">tovren</div>
      <div class="body" style="top:81px;">
        <div class="h2" style="font-size:7.4px; margin-top:0;">CREDIT PROPOSAL</div>
        <div class="h3" style="font-size:5.2px; margin-top:6px;">LOAN PRODUCTS/FEATURES RECOMMENDED</div>
        <p>Based on your circumstances and the features relevant to your requirements and objectives, we recommend the following lender and product:</p>
        <p class="mf">{{brokerToolsTablesPreferredProduct}}</p>
        <p style="margin-top:5px;">* Interest rates, fees and repayments may change if the lender changes its loan terms.</p>
        <p class="mf" style="margin-top:4px;">{%brokerToolsChartsAmortization}</p>
        <p>* If an offset account is available for your recommended loan/s, the above graph compares a loan operating without an offset account against a loan linked with an offset account. This calculation is based on your initial offset balance and estimated monthly offset contribution.</p>
        <div class="h3" style="font-size:4px;">PRODUCT SUITABILITY</div>
        <p class="mf">{Brokertools.productsuitability.isunsuitable} {Brokertools.productsuitability.isproductinconsistent}</p>
        <div class="h3" style="font-size:5.2px; margin-top:6px;">WHY OUR RECOMMENDATION MEETS YOUR BEST INTERESTS</div>
        <div class="h3" style="font-size:4px;">OPTIONS PRESENTED AND RECOMMENDATION COMMENTS</div>
        <p class="mf">{Brokertools.advicecomments.optionsandrecommendations}</p>
        <div class="h3" style="font-size:4px;">EXPLANATION FOR SELECTING INTEREST ONLY REPAYMENT (IF APPLICABLE)</div>
        <p class="mf">{Brokertools.advicecomments.interestonlyproduct}</p>
        <div class="h3" style="font-size:4px;">EXPLANATION FOR SELECTING FIXED RATE PRODUCT (IF APPLICABLE)</div>
        <p class="mf">{Brokertools.advicecomments.optionsandrecommendations}</p>
        <div class="h3" style="font-size:4px;">LINE OF CREDIT COMMENTS (IF APPLICABLE)</div>
        <p class="mf" style="margin-bottom:0;">{Brokertools.advicecomments.lineofcredit}</p>
        <div class="h3" style="font-size:4px; margin-top:1px;">INTEREST IN ADVANCE COMMENTS (IF APPLICABLE)</div>
        <p class="mf">{Brokertools.advicecomments.interestinadvance}</p>
        <div class="h3" style="font-size:5.2px;">CONFLICT OF INTEREST DISCLOSURE</div>
        <p class="mf">{{assetFinanceToolsTablesConflictOfInterest}}</p>
        <div class="h3" style="font-size:5.2px; margin-top:6px;">SECURITY TO BE PROVIDED BY YOU</div>
        <p class="mf">{{brokerToolsTablesSecurityDetails}}</p>
        <div class="h3" style="font-size:5.2px; margin-top:6px;">FUNDING WORKSHEET</div>
        <p class="mf">{{brokerToolsTablesFundingWorksheet}}</p>
        <p style="margin-top:4px;">* If you are refinancing, please refer to the Refinance Analysis which considers the costs of a refinance with the benefits you could receive from your proposed loan/s.</p>
      </div>
    </div>
    <div class="band"></div>
    <span class="band-label l">INCOME PROTECTION &amp; LIFE INSURANCE</span>
    <span class="band-label r">INCOME PROTECTION &amp; LIFE INSURANCE</span>
    <svg class="gutter-mark" width="100" height="80" viewBox="0 0 100 80"><polygon points="20,19 38,37 20,55 2,37" fill="var(--grey-mid)"/><polygon points="80,19 98,37 80,55 62,37" fill="var(--grey-mid)"/><polygon points="50,0 87,37 50,74 13,37" fill="var(--ink)"/></svg>
    <div class="footer-rule"></div>
    <span class="footer-text ft-l1">PRELIMINARY ASSESSMENT &amp; CREDIT PROPOSAL 07/2021</span>
    <span class="footer-text ft-r1">03 OF 11</span>
    <span class="footer-text ft-l2">PRELIMINARY ASSESSMENT &amp; CREDIT PROPOSAL 07/2021</span>
    <span class="footer-text ft-r2">04 OF 11</span>
  </section>

  <!-- Spread: pages 05–06 -->
  <section class="spread" style="left:769px; top:1432px;">
    <div class="page left">
      <div class="page-logo">tovren</div>
      <div class="body" style="top:83px;">
        <div class="h3" style="font-size:5.4px; margin-top:0;">ESTIMATED FEES &amp; CHARGES PAYABLE BY YOU FOR YOUR LOAN/S</div>
        <p>An estimate of the total fees and charges that may be payable by you to the lender in relation to applying for the loan/s are listed in the table below.</p>
        <p class="mf">{{brokerToolsTablesFundsAfterFees}}</p>
        <p style="margin-top:4px;">*These fees and charges are one-off payments unless otherwise indicated. These amounts are estimates only and the final figures will be shown in the credit contract issued by the lender. Some or all of these fees and charges may be payable from the loan proceeds.</p>
        <div class="h3" style="font-size:5.4px;">ESTIMATED FEES PAYABLE BY YOU TO US</div>
        <p>If a fee is payable by you, this will have been disclosed in the Credit Quote we have previously given to you. The Credit Quote will outline any fees payable for providing credit assistance and the time that they are payable. If you did not receive a Credit Quote, this will indicate that no fees are payable.</p>
        <div class="h3" style="font-size:5.4px;">HOW ARE WE PAID?</div>
        <p>We are remunerated by commission from your recommended lender and this is generally by way of both an upfront and trail commission based on your loan amount.</p>
        <p>Upfront commission is a one-off commission paid after settlement with a maximum upfront commission of 1.5%.</p>
        <p>Trail commission is an ongoing commission paid generally over the life of the loan and is based on the monthly balance of your loan amount. Trail commission is a maximum of 0.5% per annum.</p>
        <p>Commissions are paid based on a percentage of the loan drawn down. In most cases net of any offset amount. The way commissions are calculated and paid to us by lenders may vary. By following the responsible lending and best interests obligations, we will ensure that the loan/s recommended to you is not unsuitable to your requirements and objectives.</p>
        <p>These commissions may be shared between {organization.license.institution1}, the Broker and any referring party (as disclosed in this Preliminary Assessment &amp; Credit Proposal).</p>
        <p>We are not eligible for volume bonuses in relation to the loan/s.</p>
        <div class="h3" style="font-size:5.4px; margin-top:6px;">OTHER FEES/BENEFITS WE MAY BE ENTITLED TO BE PAID</div>
        <p>Other benefits may be received from our panel of lenders from time to time. These benefits may include benefits such as attendance at social events, higher servicing standards from lenders and training and educational opportunities.</p>
        <p>You are entitled to ask your Broker if any additional fees or benefits may be applicable to your credit application.</p>
      </div>
    </div>
    <div class="page right">
      <div class="page-logo">tovren</div>
      <div class="body" style="top:83px;">
        <div class="h3" style="font-size:5.4px; margin-top:0;">REASONABLE ESTIMATE OF COMMISSION</div>
        <p>An estimate of commission to be received by the Licensee from the lender for assisting you to obtain the finance are listed in the table below.</p>
        <p>We may receive an upfront commission, payable shortly after settlement.</p>
        <p>We also receive a monthly commission calculated as the percentage of the outstanding loan balance. Details of these commissions are listed in the table below.</p>
        <p>An estimate of referral fees payable by us to any third parties are also listed in the table below.</p>
        <p class="mf">{{brokerToolsTablesCommissions}}</p>
        <div class="h3" style="font-size:5.4px; margin-top:7px;">ADDITIONAL COMMENTARY RELEVANT TO YOUR CIRCUMSTANCES</div>
        <div class="h3" style="font-size:4px; margin-top:6px;">BORROWING POWER COMMENTARY</div>
        <p class="mf">{Brokertools.advicecomments.borrowingpower}</p>
        <div class="h3" style="font-size:4px; margin-top:6px;">DEPOSIT/EQUITY COMMENTS</div>
        <p class="mf">{Brokertools.advicecomments.depositorequity}</p>
        <div class="h3" style="font-size:4px; margin-top:6px;">CREDIT HISTORY COMMENTS</div>
        <p class="mf">{Brokertools.advicecomments.credithistory}</p>
        <div class="h3" style="font-size:4px; margin-top:6px;">SECURITY (PROPERTY) NOTES</div>
        <p class="mf">{Brokertools.advicecomments.security}</p>
        <div class="h3" style="font-size:4px; margin-top:6px;">LIVING EXPENSES COMMENTS</div>
        <p class="mf">{Brokertools.advicecomments.livingexpenses}</p>
      </div>
    </div>
    <div class="band"></div>
    <span class="band-label l">INCOME PROTECTION &amp; LIFE INSURANCE</span>
    <span class="band-label r">INCOME PROTECTION &amp; LIFE INSURANCE</span>
    <svg class="gutter-mark" width="100" height="80" viewBox="0 0 100 80"><polygon points="20,19 38,37 20,55 2,37" fill="var(--grey-mid)"/><polygon points="80,19 98,37 80,55 62,37" fill="var(--grey-mid)"/><polygon points="50,0 87,37 50,74 13,37" fill="var(--ink)"/></svg>
    <div class="footer-rule"></div>
    <span class="footer-text ft-l1">PRELIMINARY ASSESSMENT &amp; CREDIT PROPOSAL 07/2021</span>
    <span class="footer-text ft-r1">05 OF 11</span>
    <span class="footer-text ft-l2">PRELIMINARY ASSESSMENT &amp; CREDIT PROPOSAL 07/2021</span>
    <span class="footer-text ft-r2">06 OF 11</span>
  </section>

  <!-- Spread: pages 07–08 -->
  <section class="spread" style="left:110px; top:1953px;">
    <div class="page left">
      <div class="page-logo">tovren</div>
      <div class="body" style="top:83px;">
        <div class="h2" style="margin-top:0;">INSURANCE DECLARATION</div>
        <p class="just" style="margin-bottom:0;">To ensure we have taken the appropriate duty of care when arranging finance on your behalf, we must make you aware of the need to protect yourself, your family and your business from the possible financial hardship caused by death, disability, trauma or personal injury.</p>
        <p class="just">If you do not have adequate risk insurance in place, you may not be able to make the repayments on your loan/s if you had an accident or illness that stopped you working, or in the event of permanent disability or death. It is important that you understand the risks of not maintaining sufficient insurance to protect your loan/s and your assets.</p>
        <p style="margin-top:4px;">I/We acknowledge that my/our Broker has brought this to our attention</p>
        <p style="margin-top:4px;">I/We understand that insurance is not compulsory and is not a condition of the loan/s being approved</p>
        <p style="margin-top:4px;">I/We have considered the risks and are satisfied with the current level of personal insurance protection or have made my/our own arrangements</p>
        <p>OR</p>
        <p>I/We have considered the risks and would like to discuss the insurance options with someone recommended by my/our Broker</p>
        <div class="h2" style="margin-top:7px;">CLIENT ACKNOWLEDGEMENT</div>
        <p class="just">By signing this Preliminary Assessment &amp; Credit Proposal, you agree and acknowledge that this assessment is based on the requirements and objectives, income and expenses which you have provided to {organization.license.institution1}.</p>
        <p class="just" style="margin-top:4px;">You should check carefully that the information provided in this document and its appendices is accurate and up-to-date and that there is no omissions or inaccuracies (including any foreseeable changes to your financial situation) which may impact on your ability to meet the payment requirements in the credit contract for which you have applied.</p>
        <p class="mf" style="margin-top:6px;">{{dealTablesSignatures}}</p>
      </div>
    </div>
    <div class="page right">
      <div class="page-logo">tovren</div>
      <div class="body" style="top:83px;">
        <div class="h2" style="margin-top:0;">APPENDIX 1:<br>RISK/BENEFITS STATEMENTS</div>
        <p class="mf">{{brokerToolsDocumentsRiskBenefit}}</p>
        <div class="h2" style="margin-top:6px;">APPENDIX 2: REFINANCE ANALYSIS</div>
        <p class="mf" style="margin-top:6px;">{{brokerToolsTablesRefinanceAnalysis}}</p>
        <p class="mf">{{brokerToolsTablesRefinanceAnalysisBenefit}}</p>
        <p class="mf">{{brokerToolsTablesRefinanceAnalysisAdditionalMonthlyRepayment}}</p>
        <p class="mf">{{brokerToolsTablesRefinanceAnalysisReasons}}</p>
        <p>* If you are not refinancing, this Refinance Analysis has been intentionally left blank.</p>
      </div>
    </div>
    <div class="band"></div>
    <span class="band-label l">INCOME PROTECTION &amp; LIFE INSURANCE</span>
    <span class="band-label r">INCOME PROTECTION &amp; LIFE INSURANCE</span>
    <svg class="gutter-mark" width="100" height="80" viewBox="0 0 100 80"><polygon points="20,19 38,37 20,55 2,37" fill="var(--grey-mid)"/><polygon points="80,19 98,37 80,55 62,37" fill="var(--grey-mid)"/><polygon points="50,0 87,37 50,74 13,37" fill="var(--ink)"/></svg>
    <div class="footer-rule"></div>
    <span class="footer-text ft-l1">PRELIMINARY ASSESSMENT &amp; CREDIT PROPOSAL 07/2021</span>
    <span class="footer-text ft-r1">07 OF 11</span>
    <span class="footer-text ft-l2">PRELIMINARY ASSESSMENT &amp; CREDIT PROPOSAL 07/2021</span>
    <span class="footer-text ft-r2">08 OF 11</span>
  </section>

  <!-- Spread: pages 09–10 -->
  <section class="spread" style="left:769px; top:1953px;">
    <div class="page left">
      <div class="page-logo">tovren</div>
      <div class="body list-mf" style="top:83px;">
        <div class="h2" style="margin-top:0;">APPENDIX 3: CLIENT NEEDS ANALYSIS</div>
        <div class="h3" style="font-size:5px; margin:6px 0 6px;">PERSONAL DETAILS</div>
        <p>{{contactTablesContact1GeneralDetails}}</p>
        <p>{{contactTablesContact1ContactDetails}}</p>
        <p>{{contactTablesContact1AddressDetails}}</p>
        <p>{{contactTablesContact1Identification}}</p>
        <p>{{contactTablesContact1FamilyRelations}}</p>
        <p>{{contactTablesContact1NextOfKin}}</p>
        <p>{{contactTablesContact2GeneralDetails}}</p>
        <p>{{contactTablesContact2ContactDetails}}</p>
        <p>{{contactTablesContact2AddressDetails}}</p>
        <p>{{contactTablesContact2Identification}}</p>
        <p>{{contactTablesContact2FamilyRelations}}</p>
        <p>{{contactTablesContact2NextOfKin}}</p>
        <p>{{contactTablesContact3GeneralDetails}}</p>
        <p>{{contactTablesContact3ContactDetails}}</p>
        <p>{{contactTablesContact3AddressDetails}}</p>
        <p>{{contactTablesContact3Identification}}</p>
        <p>{{contactTablesContact3FamilyRelations}}</p>
        <p>{{contactTablesContact3NextOfKin}}</p>
        <p>{{contactTablesContact4GeneralDetails}}</p>
        <p>{{contactTablesContact4ContactDetails}}</p>
        <p>{{contactTablesContact4AddressDetails}}</p>
      </div>
    </div>
    <div class="page right">
      <div class="page-logo">tovren</div>
      <div class="body" style="top:81px;">
        <div class="h3" style="font-size:5.2px; margin-top:0;">INCOME</div>
        <p class="mf">{{contactTablesAnnualIncomeSummary}}</p>
        <div class="h3" style="font-size:5.2px; margin-top:6px;">EXPENSES</div>
        <p class="mf">{{dealTablesExpensesByHouseholdWithComments}}</p>
        <div class="h3" style="font-size:5.2px; margin-top:6px;">ASSETS</div>
        <p class="mf">{{dealTablesAssets}}</p>
        <div class="h3" style="font-size:5.2px; margin-top:4px;">LIABILITIES</div>
        <p class="mf">{{dealTablesLiabilitiesExtended}}</p>
        <p style="margin-top:4px;">* The credit card monthly repayment is calculated at a rate of 3.8% of the credit card limit.</p>
        <div class="h3" style="font-size:5.2px; margin-top:1px;">INSURERS</div>
        <p class="mf">{{contactTablesAnnualIncomeSummary}}</p>
        <div class="h3" style="font-size:5.2px; margin-top:6px;">OTHER ADVISERS</div>
        <p class="mf">{{dealTablesOtherAdvisers}}</p>
        <div class="h3" style="font-size:5.2px; margin-top:6px;">POSSIBLE CHANGES TO FINANCIAL SITUATION</div>
        <p class="mf" style="margin:0;">{{dealTablesAdverseChangesInFinancialSituation}}</p>
        <p class="mf">{{dealTablesBeneficialChangesInFinancialSituation}}</p>
        <div class="h3" style="font-size:5.2px; margin-top:6px;">EXIT STRATEGY</div>
        <p class="mf">{{dealTablesExitStrategy}}</p>
        <div class="h3" style="font-size:5.2px; margin-top:8px;">YOUR FINANCIAL SECURITY</div>
        <p class="mf">{{dealTablesYourFinancialSecurityNew}}</p>
        <div class="h3" style="font-size:5.2px; margin-top:6px;">YOUR CREDIT HISTORY</div>
        <p class="mf">{{dealTablesYourCreditHistoryNew}}</p>
        <div class="h3" style="font-size:5.2px; margin-top:6px;">VERIFICATIONS COMPLETED</div>
        <p class="mf" style="margin-bottom:1px;">{{brokerToolsTablesInterviewDetails}}</p>
        <p class="mf">{{brokerToolsTablesVerificationsCompleted}}</p>
      </div>
    </div>
    <div class="band"></div>
    <span class="band-label l">INCOME PROTECTION &amp; LIFE INSURANCE</span>
    <span class="band-label r">INCOME PROTECTION &amp; LIFE INSURANCE</span>
    <svg class="gutter-mark" width="100" height="80" viewBox="0 0 100 80"><polygon points="20,19 38,37 20,55 2,37" fill="var(--grey-mid)"/><polygon points="80,19 98,37 80,55 62,37" fill="var(--grey-mid)"/><polygon points="50,0 87,37 50,74 13,37" fill="var(--ink)"/></svg>
    <div class="footer-rule"></div>
    <span class="footer-text ft-l1">PRELIMINARY ASSESSMENT &amp; CREDIT PROPOSAL 07/2021</span>
    <span class="footer-text ft-r1">09 OF 11</span>
    <span class="footer-text ft-l2">PRELIMINARY ASSESSMENT &amp; CREDIT PROPOSAL 07/2021</span>
    <span class="footer-text ft-r2">10 OF 11</span>
  </section>

</div>
</body>
</html>
```